Logo/Stationary for Personal Injury Law Firm

We need a logo for our firm and stationary (letterhead, business cards, envelopes) to feature it. We are a personal injury firm that is branching off and starting on our own. Our firm name is "Halvorsen Law, P.C." We would like to take a more modern approach with the design, but still look professional. Our firm takes a very personal approach with all of our clients.
Updates
Here is the info located in the supported file (if you couldnt access it): 4127 North Birchwood Lane Oklahoma City, Oklahoma 73482 Telephone: (405) 362-8140 Fax: (405) 362-8177 Toll Free: (866) 362-8140 Website: www.HalvorsenLaw.example Email: name@halvorsenlaw.example Attorneys: Garrett Halvorsen – licensed to practice in Oklahoma Dustin Pellow – licensed to practice in Oklahoma Of Counsel Cyrus Ponder – licensed to practice in Texas Stefan Ruokola – licensed to practice in New York
Halvorsen Law, P.C.
I have attached an example of the letterhead from our old firm. The main attorneys (Garrett & Dustin) should come first and the of counsel attorneys should be second because they just assist with cases. But please don't let this example box you in to a certain concept.
Target Market(s)
Potential clients involved in personal injury cases (auto accidents, pharmaceutical litigation, medical malpractice & nursing home negligence).
Industry/Entity Type
Lawyer
Requirements
Must have
- Logo - Firm name "Halvorsen Law, P.C."
- Letterhead - Please see the supporting file containing all the information that needs to be presented.
- Business Card - name, title (attorney/legal assistant), address, telephone, fax, email, website
- Envelope - Logo and address
Should not have
- All of the attorneys are male, so we aren''t interested in any feminine designs.
- Please do not use any scales, gavels or family crest designs.

```html
<!DOCTYPE html>
<html lang="en">
<head>
<meta charset="utf-8">
<title>Halvorsen Law, P.C. — Letterhead</title>
<link rel="stylesheet" href="https://fonts.googleapis.com/css2?family=EB+Garamond:wght@400;500;600;700&display=swap">
<style>
  :root {
    --ink: #111111;
    --brand-blue: #1a2fd0;
    --paper: #ffffff;
    --frame: #222222;
  }
  * { margin: 0; padding: 0; box-sizing: border-box; }
  html, body {
    width: 1024px; height: 1200px; overflow: hidden;
    background: var(--paper);
    font-family: "EB Garamond", Garamond, Georgia, serif;
    color: var(--ink);
  }
  .letterhead {
    position: absolute; left: 0; top: 0;
    width: 921px; height: 1200px;
    border: 1px solid var(--frame);
    background: var(--paper);
  }
  .brand-square {
    position: absolute; left: 190px; top: 78px;
    width: 78px; height: 78px;
    background: var(--brand-blue);
  }
  .firm-name {
    position: absolute; left: 69px; top: 170px;
    font-size: 40px; font-weight: 600;
    font-variant: small-caps; letter-spacing: 0.5px;
    line-height: 1; white-space: nowrap;
  }
  .firm-contact {
    position: absolute; right: 68px; top: 76px;
    text-align: right; font-style: normal;
  }
  .firm-address {
    font-size: 15.5px; font-weight: 600; line-height: 20px;
  }
  .firm-lines {
    margin-top: 18px;
    font-size: 12.5px; line-height: 16.3px;
  }
  .roster {
    position: absolute; left: 70px; top: 1079px;
    width: 800px; height: 80px;
  }
  .roster-label {
    position: absolute; top: 0;
    font-size: 15px;
  }
  .attorney {
    position: absolute; top: 24px; white-space: nowrap;
  }
  .attorney-name { font-size: 15.5px; font-weight: 700; line-height: 18px; }
  .attorney-license { font-size: 14px; line-height: 18px; }
</style>
</head>
<body>
  <main class="letterhead">
    <div class="brand-square" aria-hidden="true"></div>
    <h1 class="firm-name">Halvorsen Law, P.C.</h1>

    <address class="firm-contact">
      <div class="firm-address">
        4127 North Birchwood Lane<br>
        Oklahoma City, Oklahoma 73482
      </div>
      <div class="firm-lines">
        Telephone: (405) 362-8140<br>
        Fax: (405) 362-8177<br>
        Toll Free: (866) 362-8140<br>
        Website: www.HalvorsenLaw.example<br>
        Email: name@halvorsenlaw.example
      </div>
    </address>

    <footer class="roster">
      <div class="roster-label" style="left:0">Attorneys:</div>
      <div class="roster-label" style="left:420px">Of Counsel:</div>

      <div class="attorney" style="left:0">
        <div class="attorney-name">Garrett Halvorsen</div>
        <div class="attorney-license">licensed to practice in Oklahoma</div>
      </div>
      <div class="attorney" style="left:211px">
        <div class="attorney-name">Dustin Pellow</div>
        <div class="attorney-license">licensed to practice in Oklahoma</div>
      </div>
      <div class="attorney" style="left:420px">
        <div class="attorney-name">Cyrus Ponder</div>
        <div class="attorney-license">licensed to practice in Texas</div>
      </div>
      <div class="attorney" style="left:599px">
        <div class="attorney-name">Stefan Ruokola</div>
        <div class="attorney-license">licensed to practice in New York</div>
      </div>
    </footer>
  </main>
</body>
</html>
```